Presentation Brochure and Sample Box Design for Kore Sheet

Kore Sheet is a colour coated solid aluminium panel that our company supplies to the signage and building cladding industries.
We require an, A4 double-sided folding brochure (swatch book) that folds 3 ways, opening once and then a second time to lay out 3 pages flat.

There should be a front and back cover.

The inside cover should be reserved with text blocks for written information about the panel.

The opposite page on the right when you first open the brochure should have all our Matte PVDF 2mm colours which you will find in the attached PDF of colour swatches and details.

When the brochure is folded out a second time, showing all three inside pages flat, the two inside pages on the right (next to the inside cover with the written information) should show all our FEVE Gloss 1.6mm colours which you will also find in the attached PDF colour book.

This brochure should have a modern and professional feel suitable for presenting to architects and designers.

We also require a box design to contain aluminium samples of all the colours in the range.

Please refer to the template attached for the box dimensions and layout.

The box should tie in with the brochure as a complete package with a modern and professional look suitable for presenting to architects and designers.

Finally we require a small label sticker to be stuck on the back of each sample. On the sticker should be the Kore Sheet logo, a space to put the product code for the sample colour and the phone number 1300 584 963.

To summarise, this package project includes:
1 tri-folding A4 brochure,
1 sample box package design,
1 sample sticker label.

This is our signature new product that we will be marketing to signage installers to create coloured and printed aluminium signs. We are also looking to move further into the building and architectural market place with this product.

Please refer to the attachments for the Kore Sheet logo - the colour swatch book and template for the sample box.
The Kore Sheet logo can be shown in White, Black or Silver.

Target Market(s)

Architects, interior designers, builders and signage installers.

Font styles to use
Serif
Sans Serif

Requirements
Must have
• A modern, neat and professional upmarket look suitable for presenting to architects.
Nice to have
• A slick and classy look that makes you want to take home the box or brochure even if you're not interested in the product.
Should not have
• A cheap, untidy, low market look with too many colours.

```html
<!DOCTYPE html>
<html lang="en">
<head>
<meta charset="utf-8">
<title>Kore Sheet – Swatch Brochure</title>
<link href="https://fonts.googleapis.com/css2?family=Lato:wght@300;400;700&family=Cormorant+Garamond:ital,wght@0,400;1,400&display=swap" rel="stylesheet">
<style>
  :root{
    --bg:#e6e6e6;
    --paper:#ffffff;
    --ink:#5a5d62;
    --ink-soft:#8a8d92;
    --fold:#dfe2e7;
    --fold-dark:#cdd1d8;
    --photo-light:#d8dadd;
    --photo-mid:#a9adb3;
    --photo-dark:#6f747a;
    --serif:"Cormorant Garamond", Georgia, serif;
    --sans:"Lato", Arial, sans-serif;
  }
  *{box-sizing:border-box;margin:0;padding:0}
  html,body{width:1200px;height:675px;overflow:hidden;background:var(--bg)}
  body{display:flex;align-items:center;justify-content:center;font-family:var(--sans)}

  .brochure{display:flex;width:900px;height:585px;box-shadow:0 10px 30px rgba(0,0,0,.12)}
  .panel{width:300px;height:100%;position:relative;overflow:hidden}

  /* Swatch panel */
  .panel--swatches{background:var(--paper);padding:34px 26px 24px}
  .swatches__title{font-family:var(--serif);font-style:italic;font-size:21px;color:var(--ink);line-height:1.05}
  .swatches__spec{font-family:var(--sans);font-weight:300;font-size:15px;letter-spacing:.5px;color:var(--ink);margin-left:22px;margin-top:2px}
  .swatches__grid{display:grid;grid-template-columns:1fr 1fr;column-gap:18px;margin-top:18px}
  .swatches__col{display:flex;flex-direction:column;gap:7px}
  .swatches__col--right{margin-top:-18px}
  .swatch{height:38px;position:relative;display:flex;align-items:flex-end;padding:0 0 4px 6px;
          font-size:7.5px;letter-spacing:.4px;text-transform:uppercase;color:#fff}
  .swatch--light{color:#333;border:1px solid #d6d6d6}
  .swatch--metal{background-image:radial-gradient(rgba(255,255,255,.25) 1px,transparent 1px);background-size:3px 3px}

  /* Fold / back cover panel */
  .panel--back{background:linear-gradient(100deg,var(--fold-dark) 0%,var(--fold) 40%,#eceef1 100%);
               display:flex;flex-direction:column;align-items:center;justify-content:flex-end;padding-bottom:70px;text-align:center}
  .brand{font-family:var(--sans);font-weight:400;letter-spacing:3px;text-transform:uppercase}
  .panel--back .brand{font-size:26px;color:#fff}
  .contact{margin-top:14px;font-size:8.5px;line-height:1.6;color:#fff}

  /* Front cover panel */
  .panel--cover{background:var(--paper)}
  .panel--cover .brand{position:absolute;top:22px;right:22px;font-size:20px;color:var(--ink-soft)}
  .cover__photo{position:absolute;left:0;top:95px;width:300px;height:370px;
                background:linear-gradient(135deg,var(--photo-light) 0%,var(--photo-mid) 45%,var(--photo-dark) 70%,var(--photo-light) 100%);
                clip-path:polygon(0 0,42% 0,30% 60%,60% 0,100% 0,100% 100%,10% 100%,0 90%)}
  .cover__note{position:absolute;right:16px;top:275px;width:128px;height:128px;border-radius:50%;
               background:rgba(215,217,220,.88);color:#fff;font-size:9.5px;line-height:1.35;
               display:flex;align-items:center;justify-content:center;text-align:center;padding:16px}
  .cover__heading{position:absolute;left:0;right:0;bottom:62px;text-align:center;font-weight:300;
                  font-size:21px;letter-spacing:1px;color:var(--ink)}
  .cover__sub{position:absolute;left:0;right:0;bottom:42px;text-align:center;font-family:var(--serif);
              font-size:13px;color:var(--ink-soft)}
</style>
</head>
<body>
<main class="brochure">

  <section class="panel panel--swatches">
    <h2 class="swatches__title">Colour coated solid aluminium</h2>
    <p class="swatches__spec">PVDF MATTE 2MM</p>
    <div class="swatches__grid">
      <div class="swatches__col">
        <div class="swatch swatch--light" style="background:#fff">White</div>
        <div class="swatch" style="background:#0c0c0e">Black</div>
        <div class="swatch" style="background:#d22034">Red</div>
        <div class="swatch" style="background:#283582">Reflex Blue</div>
        <div class="swatch" style="background:#ee5a27">Orange</div>
        <div class="swatch" style="background:#14234d">Navy Blue</div>
        <div class="swatch" style="background:#1b2459">Galaxy</div>
        <div class="swatch" style="background:#e2d5ae">Ivory</div>
        <div class="swatch" style="background:#f9b21d">Mustard</div>
        <div class="swatch" style="background:#c61f32">Plum Red</div>
      </div>
      <div class="swatches__col swatches__col--right">
        <div class="swatch" style="background:#353b42">Steel Grey</div>
        <div class="swatch" style="background:#636970">Iron Grey</div>
        <div class="swatch" style="background:#a3a6aa">Warm Grey</div>
        <div class="swatch" style="background:#c4c6c9">Smokey Grey</div>
        <div class="swatch" style="background:#dedad0">Cream</div>
        <div class="swatch swatch--metal" style="background-color:#b9bbbe">Metallic Silver</div>
        <div class="swatch swatch--metal" style="background-color:#4f5154">Metallic Charcoal</div>
        <div class="swatch swatch--metal" style="background-color:#bda470">Metallic Gold</div>
        <div class="swatch swatch--metal" style="background-color:#e6d22a">Metallic Yellow</div>
        <div class="swatch swatch--metal" style="background-color:#1d6dba">Metallic Blue</div>
      </div>
    </div>
  </section>

  <section class="panel panel--back">
    <p class="brand">Kore Sheet</p>
    <p class="contact">1300 584 963<br>48 Harbour Lane, Port Avery<br>www.koresheet.com</p>
  </section>

  <section class="panel panel--cover">
    <p class="brand">Kore Sheet</p>
    <div class="cover__photo" role="img" aria-label="Photograph of a faceted aluminium panel building facade with glass"></div>
    <p class="cover__note">Aluminium panels refers to a covering used on one material for providing protection as well as decorative look.</p>
    <h1 class="cover__heading">ALUMINIUM PANELS</h1>
    <p class="cover__sub">A new trend in the construction</p>
  </section>

</main>
</body>
</html>
```